Marlowe's Classic Dressing

We are looking for a new label as we switch or glass bottle from a traditional bottle to a round bottle. We want to create a newer/ more appealing logo, while still maintaining some of our old label features to ensure that the brand awareness is not lost. We like the coloring of the blue and white, but feel free to play around with other colors in the design.
We are looking to add product features to our label such as "Gluten-Free", "Original Recipe From 1957" "Family Owned". With this being an older company we would like to keep the traditional feel of our label with some added modern touches.
We are not married to the greek logo/ building but would love some designs with and without it.
WE ARE LOOKING FOR A ROUND LABEL. The pictures provided below are of the old bottle.
There is a picture of the ringneck bottle below. The size of the label is 4.00 x 7.00.

```html
<!DOCTYPE html>
<html lang="en">
<head>
<meta charset="utf-8">
<title>Marlowe's Greek Dressing – Label Options</title>
<link rel="stylesheet" href="https://fonts.googleapis.com/css2?family=Josefin+Sans:wght@400;600&family=Pinyon+Script&display=swap">
<style>
  :root {
    --page: #ffffff;
    --navy: #1f2858;
    --navy-light: #2b3770;
    --gold: #c9a75e;
    --gold-dark: #a8853f;
    --cream: #f4f1ea;
  }
  * { box-sizing: border-box; margin: 0; padding: 0; }
  html, body {
    width: 1200px;
    height: 1091px;
    overflow: hidden;
    background: var(--page);
  }
  .label-sheet {
    width: 1200px;
    height: 1091px;
    display: flex;
    justify-content: center;
    align-items: center;
    gap: 120px;
  }
  .label {
    position: relative;
    width: 380px;
    height: 665px;
    background: linear-gradient(90deg, var(--navy) 0%, var(--navy-light) 50%, var(--navy) 100%);
    display: flex;
    flex-direction: column;
    align-items: center;
    color: var(--cream);
    font-family: "Josefin Sans", sans-serif;
  }
  .key-band {
    position: absolute;
    left: 0;
    width: 100%;
    height: 26px;
    background: linear-gradient(180deg, var(--gold-dark), var(--gold), var(--gold-dark));
    opacity: 0.85;
  }
  .key-band--top { top: 28px; }
  .key-band--bottom { bottom: 28px; }
  .brand-name {
    margin-top: 108px;
    font-size: 44px;
    font-weight: 600;
    color: var(--gold);
    letter-spacing: 1px;
  }
  .emblem {
    margin-top: 26px;
    width: 112px;
    height: 112px;
    border-radius: 50%;
    border: 5px solid var(--gold);
    background: radial-gradient(circle, #c7ccd9 0%, #6c7594 60%, #2b3560 100%);
  }
  .product-name {
    font-size: 96px;
    font-weight: 400;
    line-height: 1;
    letter-spacing: 2px;
    color: var(--cream);
  }
  .label--plain .product-name { margin-top: 72px; }
  .label--emblem .product-name { margin-top: 30px; }
  .product-type {
    margin-top: 8px;
    font-size: 33px;
    letter-spacing: 9px;
    padding-left: 9px;
  }
  .heritage {
    margin-top: 42px;
    font-family: "Pinyon Script", cursive;
    font-size: 27px;
    color: var(--gold);
    padding: 0 16px 6px;
    border-bottom: 1px solid rgba(201, 167, 94, 0.5);
  }
  .label--emblem .heritage { margin-top: 28px; }
  .feature {
    font-size: 14px;
    letter-spacing: 2.5px;
    color: var(--cream);
  }
  .feature--owned { margin-top: 42px; }
  .label--emblem .feature--owned { margin-top: 30px; }
  .feature--gluten {
    margin-top: 22px;
    display: flex;
    align-items: center;
    gap: 12px;
  }
  .feature--gluten::before,
  .feature--gluten::after {
    content: "";
    width: 26px;
    height: 1px;
    background: rgba(244, 241, 234, 0.6);
  }
</style>
</head>
<body>
  <main class="label-sheet">
    <section class="label label--plain">
      <div class="key-band key-band--top" role="img" aria-label="Gold Greek key border pattern"></div>
      <p class="brand-name">Marlowe's</p>
      <h1 class="product-name">GREEK</h1>
      <p class="product-type">DRESSING</p>
      <p class="heritage">Original Recipe from 1957</p>
      <p class="feature feature--owned">FAMILY OWNED</p>
      <p class="feature feature--gluten">GLUTEN-FREE</p>
      <div class="key-band key-band--bottom" role="img" aria-label="Gold Greek key border pattern"></div>
    </section>

    <section class="label label--emblem">
      <div class="key-band key-band--top" role="img" aria-label="Gold Greek key border pattern"></div>
      <p class="brand-name">Marlowe's</p>
      <div class="emblem" role="img" aria-label="Gold-ringed medallion with an illustration of a Greek temple"></div>
      <h2 class="product-name">GREEK</h2>
      <p class="product-type">DRESSING</p>
      <p class="heritage">Original Recipe from 1957</p>
      <p class="feature feature--owned">FAMILY OWNED</p>
      <p class="feature feature--gluten">GLUTEN-FREE</p>
      <div class="key-band key-band--bottom" role="img" aria-label="Gold Greek key border pattern"></div>
    </section>
  </main>
</body>
</html>
```